Bref créative
VORLAQ
Stationary Design
Simple
Tamer H. Bin Ruqail
Executive Director - Partner
P. O. Box 81726
Jeddah, 23847
Saudi Arabia
thruqail@vorlaq-mail.net
www.vorlaq-web.net
CR No. 7192836450
The CR should appear only on the stationary, and not on the business cards.
The stationary should be bilingual English and Arabic.
The Arabic text for the address information is as follows.
P. O. Box = ص. ب
Jeddah = جدة
Saudi Arabia = المملكة العربية السعودية
CR = س. ت
Numbers are the same in both languages.
I ask the designer to use best judgment in selecting the font to be used on the card.
The back of the business card, will mirror the front of it as it will be used for the Arabic information.
It will have the same information as listed above.

```html
<!DOCTYPE html>
<html lang="en">
<head>
<meta charset="utf-8">
<title>VORLAQ Stationery</title>
<link rel="stylesheet" href="https://fonts.googleapis.com/css2?family=Titillium+Web:wght@400;600;700&family=Cairo:wght@400;600&display=swap">
<style>
  :root {
    --red: #d3231c;
    --orange: #f26a21;
    --amber: #f7931e;
    --ink: #2a2a2a;
    --grey: #6b6b6b;
    --rule: #d9d9d9;
    --paper: #ffffff;
    --stage: #e9e9e9;
    --dark: #262626;
    --darker: #161616;
    --sans: "Titillium Web", Arial, sans-serif;
    --arabic: "Cairo", Tahoma, sans-serif;
  }
  * { box-sizing: border-box; margin: 0; padding: 0; }
  html, body { width: 1200px; height: 540px; overflow: hidden; }
  body { background: var(--stage); font-family: var(--sans); color: var(--ink); position: relative; }

  .sheet { position: absolute; background: var(--paper); box-shadow: 0 2px 8px rgba(0,0,0,.15); overflow: hidden; }

  .brand { display: flex; align-items: center; gap: 6px; }
  .brand-square { width: 14px; height: 14px; background: var(--red); }
  .brand-name { font-family: var(--sans); font-weight: 700; font-size: 17px; letter-spacing: 1px; color: var(--ink); line-height: 1; }
  .brand--light .brand-name { color: #fff; }
  .brand--light .brand-square { background: #fff; }

  .arabic { font-family: var(--arabic); direction: rtl; }

  /* Letterhead */
  .letterhead { left: 20px; top: 20px; width: 320px; height: 452px; }
  .letterhead-topbar { position: absolute; left: 0; right: 0; top: 0; height: 6px; background: linear-gradient(90deg, var(--red), var(--orange)); }
  .letterhead .brand { position: absolute; left: 22px; top: 24px; }
  .letterhead-accent { position: absolute; right: 0; top: 30px; width: 150px; height: 6px; background: linear-gradient(90deg, var(--orange), var(--red)); }
  .letterhead-footer { position: absolute; left: 22px; right: 22px; bottom: 20px; border-top: 1px solid var(--rule); padding-top: 7px; display: flex; justify-content: space-between; font-size: 6.5px; line-height: 1.5; color: var(--grey); }
  .letterhead-footer .arabic { text-align: right; }
  .letterhead-bottombar { position: absolute; left: 0; right: 0; bottom: 0; height: 10px; background: linear-gradient(90deg, var(--red), var(--orange)); }

  /* Folder */
  .folder { left: 360px; top: 20px; width: 320px; height: 452px; background: linear-gradient(160deg, var(--amber) 0%, var(--orange) 40%, var(--red) 100%); }
  .folder-band { position: absolute; left: 0; top: 0; width: 100%; height: 100%; }
  .folder .brand { position: absolute; left: 26px; bottom: 40px; }
  .folder .brand-name { font-size: 22px; }
  .folder .brand-square { width: 18px; height: 18px; }
  .folder-web { position: absolute; right: 26px; bottom: 44px; color: #fff; font-size: 8px; }

  /* Envelope */
  .envelope { left: 700px; top: 20px; width: 480px; height: 210px; }
  .envelope-flap { position: absolute; left: 0; top: 0; width: 100%; height: 78px; }
  .envelope .brand { position: absolute; left: 24px; bottom: 46px; }
  .envelope-address { position: absolute; left: 24px; bottom: 16px; font-size: 7px; color: var(--grey); line-height: 1.45; }
  .envelope-address-ar { position: absolute; right: 24px; bottom: 16px; font-size: 7px; color: var(--grey); line-height: 1.45; text-align: right; }

  /* Business cards */
  .card { top: 250px; width: 230px; height: 130px; }
  .card--front { left: 700px; }
  .card--back { left: 950px; }
  .card-stripe { position: absolute; top: 0; bottom: 0; width: 34px; background: linear-gradient(180deg, var(--orange), var(--red)); }
  .card--front .card-stripe { right: 0; }
  .card--back .card-stripe { left: 0; }
  .card .brand { position: absolute; top: 14px; }
  .card--front .brand { left: 14px; }
  .card--back .brand { right: 14px; }
  .card .brand-name { font-size: 14px; }
  .card .brand-square { width: 11px; height: 11px; }
  .card-person { position: absolute; top: 40px; }
  .card--front .card-person { left: 14px; }
  .card--back .card-person { right: 14px; text-align: right; }
  .card-name { font-size: 10px; font-weight: 700; color: var(--red); line-height: 1.2; }
  .card-title { font-size: 7px; color: var(--grey); }
  .card-contact { position: absolute; bottom: 12px; list-style: none; font-size: 6.6px; line-height: 1.55; color: var(--ink); }
  .card--front .card-contact { left: 14px; }
  .card--back .card-contact { right: 14px; }
  .card-contact li { display: flex; align-items: center; gap: 4px; }
  .card-contact svg { width: 7px; height: 7px; flex: none; }
  .card--back .card-name, .card--back .card-title, .card--back .card-contact { font-family: var(--arabic); }

  /* Presentation */
  .cover { left: 700px; top: 400px; width: 230px; height: 120px; background: radial-gradient(ellipse at 55% 35%, #3a3a3a, var(--darker) 75%); }
  .cover-band { position: absolute; left: 0; right: 0; bottom: 18px; height: 30px; background: linear-gradient(90deg, var(--red), var(--orange)); padding: 5px 12px; color: #fff; }
  .cover-title { font-size: 8.5px; font-weight: 700; letter-spacing: .5px; line-height: 1.2; }
  .cover-desc { font-size: 6.5px; opacity: .9; }
  .cover .brand { position: absolute; left: 12px; top: 14px; }
  .cover .brand-name { font-size: 13px; }
  .cover .brand-square { width: 10px; height: 10px; }

  .page { left: 950px; top: 400px; width: 230px; height: 120px; }
  .page-heading { position: absolute; left: 14px; top: 10px; font-size: 10px; font-weight: 700; color: var(--ink); letter-spacing: .5px; }
  .page-columns { position: absolute; left: 14px; right: 14px; top: 28px; display: flex; gap: 14px; }
  .page-col { flex: 1; font-size: 6px; line-height: 1.45; color: var(--grey); }
  .page-col h3 { font-size: 6.6px; font-weight: 700; color: var(--red); margin-top: 2px; }
  .page-col ul { list-style: none; padding-left: 6px; }
  .page-bar { position: absolute; left: 0; right: 0; bottom: 0; height: 6px; background: linear-gradient(90deg, var(--red), var(--orange)); }
  .page .brand { position: absolute; right: 12px; bottom: 12px; }
  .page .brand-name { font-size: 9px; }
  .page .brand-square { width: 7px; height: 7px; }
</style>
</head>
<body>

  <section class="sheet letterhead" aria-label="Letterhead">
    <div class="letterhead-topbar"></div>
    <div class="brand"><span class="brand-square"></span><span class="brand-name">VORLAQ</span></div>
    <div class="letterhead-accent"></div>
    <footer class="letterhead-footer">
      <div>
        P. O. Box 81726, Jeddah, 23847, Saudi Arabia<br>
        CR No. 7192836450<br>
        www.vorlaq-web.net
      </div>
      <div class="arabic">
        ص. ب 81726، جدة 23847، المملكة العربية السعودية<br>
        س. ت 7192836450<br>
        www.vorlaq-web.net
      </div>
    </footer>
    <div class="letterhead-bottombar"></div>
  </section>

  <section class="sheet folder" aria-label="Presentation folder">
    <svg class="folder-band" viewBox="0 0 320 452" preserveAspectRatio="none" aria-hidden="true">
      <polygon points="0,300 320,220 320,330 0,410" fill="rgba(0,0,0,.18)"/>
      <polygon points="0,0 320,0 320,40 0,90" fill="rgba(255,255,255,.08)"/>
    </svg>
    <div class="brand brand--light"><span class="brand-square"></span><span class="brand-name">VORLAQ</span></div>
    <div class="folder-web">www.vorlaq-web.net</div>
  </section>

  <section class="sheet envelope" aria-label="Envelope">
    <svg class="envelope-flap" viewBox="0 0 480 78" preserveAspectRatio="none" aria-hidden="true">
      <defs>
        <linearGradient id="flapGrad" x1="0" x2="1" y1="0" y2="0">
          <stop offset="0" stop-color="#d3231c"/>
          <stop offset="1" stop-color="#f26a21"/>
        </linearGradient>
      </defs>
      <path d="M0,0 H480 V50 Q240,86 0,50 Z" fill="url(#flapGrad)"/>
    </svg>
    <div class="brand"><span class="brand-square"></span><span class="brand-name">VORLAQ</span></div>
    <div class="envelope-address">
      P. O. Box 81726, Jeddah, 23847, Saudi Arabia<br>
      CR No. 7192836450 · www.vorlaq-web.net
    </div>
    <div class="envelope-address-ar arabic">
      ص. ب 81726، جدة 23847، المملكة العربية السعودية<br>
      س. ت 7192836450
    </div>
  </section>

  <section class="sheet card card--front" aria-label="Business card, English side">
    <div class="card-stripe"></div>
    <div class="brand"><span class="brand-square"></span><span class="brand-name">VORLAQ</span></div>
    <div class="card-person">
      <p class="card-name">Tamer H. Bin Ruqail</p>
      <p class="card-title">Executive Director - Partner</p>
    </div>
    <ul class="card-contact">
      <li><svg viewBox="0 0 10 10"><path d="M5 0C3 0 1.5 1.5 1.5 3.5 1.5 6 5 10 5 10s3.5-4 3.5-6.5C8.5 1.5 7 0 5 0z" fill="#d3231c"/></svg>P. O. Box 81726, Jeddah, 23847, Saudi Arabia</li>
      <li><svg viewBox="0 0 10 10"><rect x="0.5" y="2" width="9" height="6" fill="none" stroke="#d3231c"/><path d="M0.5 2 5 5.5 9.5 2" fill="none" stroke="#d3231c"/></svg>thruqail@vorlaq-mail.net</li>
      <li><svg viewBox="0 0 10 10"><circle cx="5" cy="5" r="4.3" fill="none" stroke="#d3231c"/><path d="M0.7 5H9.3M5 0.7C3 3 3 7 5 9.3M5 0.7C7 3 7 7 5 9.3" fill="none" stroke="#d3231c" stroke-width=".7"/></svg>www.vorlaq-web.net</li>
    </ul>
  </section>

  <section class="sheet card card--back" aria-label="Business card, Arabic side" dir="rtl">
    <div class="card-stripe"></div>
    <div class="brand" dir="ltr"><span class="brand-square"></span><span class="brand-name">VORLAQ</span></div>
    <div class="card-person">
      <p class="card-name">تامر ح. بن رقيل</p>
      <p class="card-title">المدير التنفيذي - شريك</p>
    </div>
    <ul class="card-contact">
      <li><svg viewBox="0 0 10 10"><path d="M5 0C3 0 1.5 1.5 1.5 3.5 1.5 6 5 10 5 10s3.5-4 3.5-6.5C8.5 1.5 7 0 5 0z" fill="#d3231c"/></svg>ص. ب 81726، جدة 23847، المملكة العربية السعودية</li>
      <li><svg viewBox="0 0 10 10"><rect x="0.5" y="2" width="9" height="6" fill="none" stroke="#d3231c"/><path d="M0.5 2 5 5.5 9.5 2" fill="none" stroke="#d3231c"/></svg><span dir="ltr">thruqail@vorlaq-mail.net</span></li>
      <li><svg viewBox="0 0 10 10"><circle cx="5" cy="5" r="4.3" fill="none" stroke="#d3231c"/><path d="M0.7 5H9.3M5 0.7C3 3 3 7 5 9.3M5 0.7C7 3 7 7 5 9.3" fill="none" stroke="#d3231c" stroke-width=".7"/></svg><span dir="ltr">www.vorlaq-web.net</span></li>
    </ul>
  </section>

  <section class="sheet cover" aria-label="Presentation cover">
    <div class="brand brand--light"><span class="brand-square"></span><span class="brand-name">VORLAQ</span></div>
    <div class="cover-band">
      <p class="cover-title">TITLE OF PRESENTATION</p>
      <p class="cover-desc">Description</p>
    </div>
  </section>

  <section class="sheet page" aria-label="Presentation inner page">
    <h2 class="page-heading">WHAT WE DO...</h2>
    <div class="page-columns">
      <div class="page-col">
        <h3>• Business Core Projects</h3>
        <ul><li>- Network planning</li><li>- Data center setup</li><li>- Systems support</li></ul>
        <h3>• Event Solutions</h3>
        <ul><li>- Stage systems</li><li>- Live streaming</li><li>- Venue support</li></ul>
      </div>
      <div class="page-col">
        <h3>• Managed Services</h3>
        <ul><li>- Cloud hosting</li><li>- Help desk</li></ul>
        <h3>• Training Services</h3>
        <ul><li>- Staff courses</li><li>- Certifications</li></ul>
      </div>
    </div>
    <div class="brand"><span class="brand-square"></span><span class="brand-name">VORLAQ</span></div>
    <div class="page-bar"></div>
  </section>

</body>
</html>
```